Kelvoranet.com Webpage Design

Design Brief for kelvoranet.com (Copy of Brief also in attached Word file)

Name of Website- kelvoranet.com (existing logo and look & feel of website to be changed)

Logo - Finalised. The logo files are attached with the brief as “logo.jpeg”. The “Blue- Grey” version of the logo is for use on lighter backgrounds and the “Orange-White” version of the logo is for use on darker backgrounds. (A full Black version of the logo is also attached). Both versions may be used in different parts of the website. All attached files are in .png format.
Status - The website in functional and is undergoing user trials. However, we want to improve the look & feel of the website so at it seems
a. cotemporary,
b. Easy to Navigate
c. professional and
d. Vibrant.

Please visit ‘kelvoranet.com’ to check out the website and its functionalities – please use it only as a reference for the features & functions to be provided, however the designer should use a ‘Free Hand’ in designing the composition of various parts of the webpage without getting too influenced by the existing design

Objective of the Website ‘kelvoranet.com –
a. It is a portal focussed on listing of ‘Retail’ specific real-estate properties by developers, owners and realty brokers. The properties shall listed under the following four categories-
i. Retail Malls
ii. Shopping Complexes
iii. High-street shops
iv. Retail Warehouses
*refer kelvoranet.com for better clarity

b. The abovementioned properties shall be listed either for ‘Sale’ or ‘rent\lease’ or both

c. Users shall visit the site in case they wish to acquire a retail \ shop space either on ‘sale’ or ‘rent’. These Users would be able to specify the ‘Search Criteria’ through the tool-bars provided on the website – the ‘Search Criteria’ shall comprise of ‘Type of space category’, ‘City’, ‘Locality’, transaction type ie ‘Rent \ Sale’ and ‘Area Range’

d. The main revenue model for the website shall be listing fee ( or advertising charges ) payable by those listing their properties on the website.

Three Main Pages of Website (kelvoranet.com) that need to be designed -
a. Main Home Page (visit the web link - http://kelvoranet.com/ ) - The main home page has the “Search Toolbar” for specifying of Search Criteria by the User. It shall also have the following features & functions-
i. Main Advertising Banner
ii. Featured Projects
iii. New Launches
iv. Toolbar with buttons – ‘Advertise with Us’, ‘Listings Alert’, ‘Quorra Desk’, ‘Advertiser Login’

b. Property Listings Page (visit the web link - http://kelvoranet.com/gurgaon-in-india ) - The List of property options that match the Criteria specified by the ‘User’ get displayed on this page.

c. Property Detail Page - When the ‘User’ clicks on the “More….” Button on the ‘Property Listings Page’ (given in point b. above) the web page with the details of the property opens. (For Example – visit the web link - http://kelvoranet.com/dorvik-Shopping-Complex-dorvik-bellmoor-gurgaon-636 )

Note:- Please refer to attached ‘Shopping’ related images the designer may use them on the website to provide a look & feel of retail if required – either separately or rotate in a single window

Target Market(s)

Retailers & Investors looking for retail space, Real Estate Brokers, Developers

Industry/Entity Type

Advertising

Number of Pages Required

3 page

Requirements
Must have
• Refer to existing site kelvoranet.com -- all the existing functionalities are a must have.
Nice to have
• The Designer may use the retail related images on the website if required for making it more vibrant. Refer attached images Shopping(1-6).jpg

```html
<!DOCTYPE html>
<html lang="en">
<head>
<meta charset="utf-8">
<title>Kelvoranet.com – India's Leading Portal for Retail Space</title>
<link href="https://fonts.googleapis.com/css2?family=Open+Sans:wght@400;600;700&family=Roboto:wght@300;400;500;700;900&display=swap" rel="stylesheet">
<style>
:root{
  --orange:#eaa43c;
  --orange-dark:#d89128;
  --ink:#333;
  --muted:#8a8a8a;
  --line:#e4e4e4;
  --panel:#f6f6f6;
  --footer:#f3f3f3;
  --white:#fff;
  --hero-top:#2a2c30;
  --hero-bottom:#4a4134;
}
*{box-sizing:border-box;margin:0;padding:0}
html,body{width:1200px;height:2702px;overflow:hidden}
body{position:relative;background:var(--white);font-family:"Open Sans",Arial,sans-serif;color:var(--ink)}
.abs{position:absolute}

/* hero */
.hero{left:0;top:0;width:1200px;height:750px;background:linear-gradient(180deg,#1f2124 0%,#3a3632 45%,#5a4a36 100%)}
.hero-shade{left:0;top:0;width:1200px;height:750px;background:radial-gradient(ellipse at 50% 30%,rgba(255,255,255,.08),rgba(0,0,0,.35))}
.brand{left:0;top:52px;width:1200px;text-align:center}
.brand-name{display:inline-flex;align-items:center;gap:12px;font-family:"Roboto",sans-serif;font-weight:500;font-size:50px;color:var(--white);letter-spacing:-.5px}
.brand-dot{width:34px;height:34px;border-radius:50%;background:var(--orange)}
.brand-tag{margin-top:2px;font-family:"Roboto",sans-serif;font-weight:700;font-size:11px;letter-spacing:1.6px;color:var(--orange)}
.top-nav{left:380px;top:180px;width:440px;display:flex;justify-content:space-between}
.top-nav a{width:140px;text-align:center;text-decoration:none}
.top-nav svg{display:block;margin:0 auto 4px}
.top-nav .nav-title{display:block;font-size:14px;font-weight:600;color:var(--orange)}
.top-nav .nav-sub{display:block;font-size:10px;color:var(--white)}
.hero-rule{left:171px;top:293px;width:858px;height:1px;background:rgba(255,255,255,.25)}
.hero-kicker{left:0;top:318px;width:1200px;text-align:center;font-family:"Roboto",sans-serif;font-weight:300;font-size:46px;letter-spacing:3px;color:#ddd}
.hero-title{left:0;top:360px;width:1200px;text-align:center;font-family:"Roboto",sans-serif;font-weight:900;font-size:78px;letter-spacing:9px;color:var(--orange)}
.hero-arrow{top:348px;width:54px;height:54px;border:2px solid rgba(255,255,255,.5);border-radius:50%;display:flex;align-items:center;justify-content:center}
.btn-register{left:360px;top:484px;width:230px;height:59px;background:var(--orange);color:var(--white);font-size:14px;display:flex;align-items:center;justify-content:center;letter-spacing:.5px}
.btn-signin{left:610px;top:484px;width:230px;height:59px;border:2px solid rgba(255,255,255,.85);color:var(--white);font-size:14px;display:flex;align-items:center;justify-content:center;letter-spacing:.5px}

/* search */
.search{left:171px;top:640px;width:858px;height:110px;background:var(--white);border-top:3px solid #111}
.field{top:20px;height:42px;border:1px solid var(--line);font-size:10px;color:#777;display:flex;align-items:center;justify-content:space-between;padding:0 14px}
.field .caret{width:0;height:0;border-left:4px solid transparent;border-right:4px solid transparent;border-top:5px solid #888}
.btn-search{left:715px;top:20px;width:122px;height:42px;background:var(--orange);color:var(--white);font-size:11px;font-weight:700;display:flex;align-items:center;justify-content:center;gap:8px}
.format-row{left:18px;top:78px;display:flex;align-items:center;font-size:11px;color:#555;white-space:nowrap}
.format-row .hint{color:var(--orange);margin-left:8px;margin-right:32px}
.check{display:inline-flex;align-items:center;gap:8px;margin-right:40px;color:#777;font-size:11px}
.check i{width:12px;height:12px;border:1px solid #bbb;display:inline-block}

/* formats */
.section-title{left:0;top:782px;width:1200px;text-align:center;font-family:"Roboto",sans-serif;font-size:40px;font-weight:400;color:#555}
.section-title b{color:var(--orange);font-weight:500}
.section-sub{left:0;top:830px;width:1200px;text-align:center;font-size:19px;color:#666}
.format{top:878px;width:210px}
.format .photo{height:203px}
.format h3{margin-top:17px;font-size:15px;font-weight:600;color:var(--orange)}
.format p{font-size:12px;color:#777;margin-top:2px}

/* section bars */
.bar{left:171px;width:858px;height:56px;background:var(--panel)}
.bar-tab{left:0;top:0;width:297px;height:56px;background:var(--orange);display:flex;align-items:center}
.bar-icon{width:50px;height:56px;background:var(--orange-dark);display:flex;align-items:center;justify-content:center}
.bar-tab h2{font-size:17px;font-weight:600;color:var(--white);margin-left:30px}
.bar-nav{right:18px;top:20px;display:flex;gap:24px}

/* cards */
.card{width:273px}
.card .photo{height:205px;position:relative}
.card .row{display:flex;justify-content:space-between;align-items:baseline;padding:0 16px}
.card .name{font-size:16px;color:var(--orange);font-weight:600;margin-top:10px}
.card .city{font-size:13px;font-weight:700;color:#222}
.card .type{font-size:11px;color:#888;padding:0 16px}
.card .meta{border-top:1px solid var(--line);margin-top:10px;padding:9px 16px 0;display:flex;justify-content:space-between;font-size:11px;color:#555}
.card .meta span{display:inline-flex;align-items:center;gap:8px}
.card .cta{margin-top:9px;height:37px;background:var(--orange);color:var(--white);font-size:13px;display:flex;align-items:center;justify-content:center}
.badge{left:14px;top:14px;width:58px;height:58px;border:2px solid var(--white);border-radius:50%;color:var(--white);font-size:11px;font-weight:700;display:flex;align-items:center;justify-content:center}
.dim{left:0;top:0;width:100%;height:100%;background:rgba(30,30,30,.55)}

.mini{width:210px}
.mini .photo{height:176px;position:relative}
.mini .row{display:flex;justify-content:space-between;align-items:baseline;padding:0 8px}
.mini .name{font-size:12px;color:var(--orange);font-weight:600;margin-top:10px}
.mini .city{font-size:10px;font-weight:700}
.mini .row2{display:flex;justify-content:space-between;padding:0 8px;font-size:9px;color:#666}
.mini .row2 span{display:inline-flex;align-items:center;gap:4px}
.mini .cta{margin-top:8px;height:30px;background:var(--orange);color:var(--white);font-size:11px;display:flex;align-items:center;justify-content:center}
.mini .badge{width:50px;height:50px;font-size:10px}

/* photo tones */
.tone-mall{background:linear-gradient(160deg,#e9e6dd,#b9c3b0 50%,#8e9a7a)}
.tone-complex{background:linear-gradient(170deg,#cfd6de,#8a98a6 55%,#5d6a77)}
.tone-warehouse{background:linear-gradient(170deg,#4a4540,#a79e90 50%,#dcd6cc)}
.tone-street{background:linear-gradient(170deg,#f3ecc8,#c5b77a 50%,#3c3a36)}
.tone-tower{background:linear-gradient(180deg,#ffffff 0%,#cfe3e0 40%,#6fa7a0 75%,#4c6e60)}
.tone-house{background:linear-gradient(180deg,#6fa6de 0%,#b9d5ec 35%,#a98d67 55%,#4d8a2c 75%,#3a7a22)}

/* footer */
.footer{left:0;top:2371px;width:1200px;height:247px;background:var(--footer)}
.fcol{top:49px;width:198px}
.fcol h4{font-family:"Roboto",sans-serif;font-size:14px;font-weight:500;color:#333;letter-spacing:.5px;padding-bottom:14px;border-bottom:1px solid var(--orange);width:198px}
.fcol p,.fcol li{font-size:11px;color:#888;line-height:17px}
.fcol ul{list-style:none;margin-top:22px}
.fcol li{line-height:22px}
.fcol .date{color:#555}
.btn-more{margin-top:14px;width:78px;height:26px;background:var(--orange);color:var(--white);font-size:10px;display:flex;align-items:center;justify-content:center}
.input-email{margin-top:12px;height:30px;border:1px solid #ddd;background:var(--white);font-size:10px;color:#777;display:flex;align-items:center;justify-content:center}
.btn-send{margin-top:4px;height:26px;background:var(--orange);color:var(--white);font-size:10px;display:flex;align-items:center;justify-content:center}
.bottom{left:0;top:2618px;width:1200px;height:84px;background:var(--white);border-top:1px solid var(--line)}
.bottom-brand{left:171px;top:26px;display:flex;align-items:center;gap:8px;font-family:"Roboto",sans-serif;font-weight:500;font-size:22px;color:#555}
.bottom-brand i{width:16px;height:16px;border-radius:50%;background:#888;display:inline-block}
.copyright{left:371px;top:34px;font-size:11px;color:#777}
.copyright span{color:var(--orange)}
.social{left:879px;top:26px;display:flex;gap:10px}
.social i{width:28px;height:28px;border-radius:50%;background:#8a8a8a;display:block}
</style>
</head>
<body>

<header>
  <div class="abs hero" role="img" aria-label="Dusk aerial view of a modern city skyline"></div>
  <div class="abs hero-shade"></div>

  <div class="abs brand">
    <div class="brand-name"><span class="brand-dot"></span>kelvoranet</div>
    <div class="brand-tag">INDIA'S LEADING PORTAL FOR RETAIL SPACE</div>
  </div>

  <nav class="abs top-nav">
    <a href="#"><svg width="20" height="20" viewBox="0 0 24 24"><path d="M12 2l3 7h7l-5.5 4.5L18.5 21 12 16.5 5.5 21l2-7.5L2 9h7z" fill="none" stroke="#eaa43c" stroke-width="1.6"/></svg><span class="nav-title">Quorra Desk</span><span class="nav-sub">Shop Search Services</span></a>
    <a href="#"><svg width="20" height="20" viewBox="0 0 24 24"><path d="M6 17V11a6 6 0 0 1 12 0v6l2 2H4z M10 21h4" fill="none" stroke="#eaa43c" stroke-width="1.6"/></svg><span class="nav-title">List Alert</span><span class="nav-sub">List Your Property Here</span></a>
    <a href="#"><svg width="20" height="20" viewBox="0 0 24 24"><path d="M3 10h4l10-5v14L7 14H3z M7 14l2 6" fill="none" stroke="#eaa43c" stroke-width="1.6"/></svg><span class="nav-title">Advertise with us</span><span class="nav-sub">Standard listing - FREE</span></a>
  </nav>

  <div class="abs hero-rule"></div>
  <div class="abs hero-kicker">INDIA'S LEADING PORTAL FOR</div>
  <div class="abs hero-title">RENTALSPACE!</div>

  <div class="abs hero-arrow" style="left:52px"><svg width="14" height="14" viewBox="0 0 14 14"><path d="M9 2L4 7l5 5" fill="none" stroke="#ddd" stroke-width="1.6"/></svg></div>
  <div class="abs hero-arrow" style="left:1086px"><svg width="14" height="14" viewBox="0 0 14 14"><path d="M5 2l5 5-5 5" fill="none" stroke="#ddd" stroke-width="1.6"/></svg></div>

  <a class="abs btn-register">REGISTER</a>
  <a class="abs btn-signin">SIGN IN</a>

  <form class="abs search">
    <div class="abs field" style="left:18px;width:122px">BOTH<span class="caret"></span></div>
    <div class="abs field" style="left:160px;width:190px">CITY<span class="caret"></span></div>
    <div class="abs field" style="left:368px;width:122px">LOCALITY<span class="caret"></span></div>
    <div class="abs field" style="left:510px;width:188px">PROJECT NAME...</div>
    <div class="abs btn-search">SEARCH <svg width="12" height="12" viewBox="0 0 14 14"><circle cx="6" cy="6" r="4.5" fill="none" stroke="#fff" stroke-width="1.6"/><path d="M9.5 9.5L13 13" stroke="#fff" stroke-width="1.6"/></svg></div>
    <div class="abs format-row">Select Retail Format :<span class="hint">Meaning of Retail Format</span>
      <span class="check"><i></i>Retail Malls</span>
      <span class="check"><i></i>Shopping Complex</span>
      <span class="check"><i></i>High Street Shops</span>
      <span class="check" style="margin-right:0"><i></i>Retail Warehouses</span>
    </div>
  </form>
</header>

<main>
  <h2 class="abs section-title"><b>Select</b> Retail <b>Format</b></h2>
  <p class="abs section-sub">Meaning of Retail Format</p>

  <div class="abs format" style="left:171px"><div class="photo tone-mall" role="img" aria-label="Bright shopping mall atrium with planters"></div><h3>Retail Malls</h3><p>Centrally Air-Conditioned</p></div>
  <div class="abs format" style="left:387px"><div class="photo tone-complex" role="img" aria-label="Multi-level shopping complex interior"></div><h3>Shopping Complex</h3><p>Non Air-Conditioned Building</p></div>
  <div class="abs format" style="left:603px"><div class="photo tone-warehouse" role="img" aria-label="Retail warehouse showroom with displays"></div><h3>Retail Warehouses</h3><p>Road Facing Retail</p></div>
  <div class="abs format" style="left:819px"><div class="photo tone-street" role="img" aria-label="High street shop interior with shelves"></div><h3>High Street Shops</h3><p>Back-end Retail Storage</p></div>

  <!-- featured projects -->
  <div class="abs bar" style="top:1180px">
    <div class="abs bar-tab"><div class="bar-icon"><svg width="18" height="18" viewBox="0 0 24 24"><path d="M12 2l3 7h7l-5.5 4.5L18.5 21 12 16.5 5.5 21l2-7.5L2 9h7z" fill="#fff"/></svg></div><h2>Featured Projects</h2></div>
    <div class="abs bar-nav"><svg width="10" height="14" viewBox="0 0 10 14"><path d="M7 2L2 7l5 5" fill="none" stroke="#ccc" stroke-width="1.6"/></svg><svg width="10" height="14" viewBox="0 0 10 14"><path d="M3 2l5 5-5 5" fill="none" stroke="#ccc" stroke-width="1.6"/></svg></div>
  </div>

  <article class="abs card" style="left:171px;top:1263px">
    <div class="photo tone-tower" role="img" aria-label="Glass office tower under a clear sky">
      <div class="abs dim"></div>
      <div class="abs badge">RENT</div>
      <svg class="abs" style="left:116px;top:80px" width="42" height="42" viewBox="0 0 42 42"><circle cx="17" cy="17" r="12" fill="none" stroke="#eaa43c" stroke-width="4"/><path d="M26 26l12 12" stroke="#eaa43c" stroke-width="5"/></svg>
    </div>
    <div class="row"><span class="name">The Orvelle Mall</span><span class="city">New Dehli</span></div>
    <div class="type">Retail Malls</div>
    <div class="meta"><span><svg width="9" height="12" viewBox="0 0 10 14"><path d="M5 0a5 5 0 0 1 5 5c0 4-5 9-5 9S0 9 0 5a5 5 0 0 1 5-5z" fill="#444"/><circle cx="5" cy="5" r="2" fill="#fff"/></svg>Lakeview Road</span><span>More</span></div>
    <div class="cta">View The Listing</div>
  </article>
  <article class="abs card" style="left:464px;top:1263px">
    <div class="photo tone-house" role="img" aria-label="Stone-front villa with lawn and trees"></div>
    <div class="row"><span class="name">The Orvelle Mall</span><span class="city">New Dehli</span></div>
    <div class="type">Retail Malls</div>
    <div class="meta"><span><svg width="9" height="12" viewBox="0 0 10 14"><path d="M5 0a5 5 0 0 1 5 5c0 4-5 9-5 9S0 9 0 5a5 5 0 0 1 5-5z" fill="#444"/><circle cx="5" cy="5" r="2" fill="#fff"/></svg>Lakeview Road</span><span>More</span></div>
    <div class="cta">View The Listing</div>
  </article>
  <article class="abs card" style="left:756px;top:1263px">
    <div class="photo tone-house" role="img" aria-label="Villa with stone chimney and garden"></div>
    <div class="row"><span class="name">The Orvelle Mall</span><span class="city">New Dehli</span></div>
    <div class="type">Retail Malls</div>
    <div class="meta"><span><svg width="9" height="12" viewBox="0 0 10 14"><path d="M5 0a5 5 0 0 1 5 5c0 4-5 9-5 9S0 9 0 5a5 5 0 0 1 5-5z" fill="#444"/><circle cx="5" cy="5" r="2" fill="#fff"/></svg>Lakeview Road</span><span>More</span></div>
    <div class="cta">View The Listing</div>
  </article>

  <article class="abs card" style="left:171px;top:1610px">
    <div class="photo tone-tower" role="img" aria-label="Green glass office towers"></div>
    <div class="row"><span class="name">The Orvelle Mall</span><span class="city">New Dehli</span></div>
    <div class="type">Retail Malls</div>
    <div class="meta"><span><svg width="9" height="12" viewBox="0 0 10 14"><path d="M5 0a5 5 0 0 1 5 5c0 4-5 9-5 9S0 9 0 5a5 5 0 0 1 5-5z" fill="#444"/><circle cx="5" cy="5" r="2" fill="#fff"/></svg>Lakeview Road</span><span>More</span></div>
    <div class="cta">View The Listing</div>
  </article>
  <article class="abs card" style="left:464px;top:1610px">
    <div class="photo tone-house" role="img" aria-label="Villa with stone chimney and lawn"></div>
    <div class="row"><span class="name">The Orvelle Mall</span><span class="city">New Dehli</span></div>
    <div class="type">Retail Malls</div>
    <div class="meta"><span><svg width="9" height="12" viewBox="0 0 10 14"><path d="M5 0a5 5 0 0 1 5 5c0 4-5 9-5 9S0 9 0 5a5 5 0 0 1 5-5z" fill="#444"/><circle cx="5" cy="5" r="2" fill="#fff"/></svg>Lakeview Road</span><span>More</span></div>
    <div class="cta">View The Listing</div>
  </article>
  <article class="abs card" style="left:756px;top:1610px">
    <div class="photo tone-house" role="img" aria-label="Villa with flowering garden"></div>
    <div class="row"><span class="name">The Orvelle Mall</span><span class="city">New Dehli</span></div>
    <div class="type">Retail Malls</div>
    <div class="meta"><span><svg width="9" height="12" viewBox="0 0 10 14"><path d="M5 0a5 5 0 0 1 5 5c0 4-5 9-5 9S0 9 0 5a5 5 0 0 1 5-5z" fill="#444"/><circle cx="5" cy="5" r="2" fill="#fff"/></svg>Lakeview Road</span><span>More</span></div>
    <div class="cta">View The Listing</div>
  </article>

  <!-- new projects -->
  <div class="abs bar" style="top:1986px">
    <div class="abs bar-tab"><div class="bar-icon"><svg width="20" height="20" viewBox="0 0 24 24"><path d="M10 2a6 6 0 0 1 6 6c0 5-6 10-6 10S4 13 4 8a6 6 0 0 1 6-6z" fill="none" stroke="#fff" stroke-width="2"/><path d="M2 22h20" stroke="#fff" stroke-width="2"/></svg></div><h2>New Projects</h2></div>
    <div class="abs bar-nav"><svg width="10" height="14" viewBox="0 0 10 14"><path d="M7 2L2 7l5 5" fill="none" stroke="#ccc" stroke-width="1.6"/></svg><svg width="10" height="14" viewBox="0 0 10 14"><path d="M3 2l5 5-5 5" fill="none" stroke="#ccc" stroke-width="1.6"/></svg></div>
  </div>

  <article class="abs mini" style="left:171px;top:2069px">
    <div class="photo tone-house" role="img" aria-label="Villa exterior with garden">
      <div class="abs dim"></div>
      <div class="abs badge">SALE</div>
      <svg class="abs" style="left:90px;top:66px" width="36" height="36" viewBox="0 0 42 42"><circle cx="17" cy="17" r="12" fill="none" stroke="#eaa43c" stroke-width="4"/><path d="M26 26l12 12" stroke="#eaa43c" stroke-width="5"/></svg>
    </div>
    <div class="row"><span class="name">The Orvelle Mall</span><span class="city">New Dehli</span></div>
    <div class="row2"><span>Retail Malls</span><span><svg width="7" height="10" viewBox="0 0 10 14"><path d="M5 0a5 5 0 0 1 5 5c0 4-5 9-5 9S0 9 0 5a5 5 0 0 1 5-5z" fill="#444"/></svg>Lakeview Road</span></div>
    <div class="cta">View The Listing</div>
  </article>
  <article class="abs mini" style="left:387px;top:2069px">
    <div class="photo tone-house" role="img" aria-label="Villa with stone chimney"></div>
    <div class="row"><span class="name">The Orvelle Mall</span><span class="city">New Dehli</span></div>
    <div class="row2"><span>Retail Malls</span><span><svg width="7" height="10" viewBox="0 0 10 14"><path d="M5 0a5 5 0 0 1 5 5c0 4-5 9-5 9S0 9 0 5a5 5 0 0 1 5-5z" fill="#444"/></svg>Lakeview Road</span></div>
    <div class="cta">View The Listing</div>
  </article>
  <article class="abs mini" style="left:603px;top:2069px">
    <div class="photo tone-tower" role="img" aria-label="Green glass office towers"></div>
    <div class="row"><span class="name">The Orvelle Mall</span><span class="city">New Dehli</span></div>
    <div class="row2"><span>Retail Malls</span><span><svg width="7" height="10" viewBox="0 0 10 14"><path d="M5 0a5 5 0 0 1 5 5c0 4-5 9-5 9S0 9 0 5a5 5 0 0 1 5-5z" fill="#444"/></svg>Lakeview Road</span></div>
    <div class="cta">View The Listing</div>
  </article>
  <article class="abs mini" style="left:819px;top:2069px">
    <div class="photo tone-house" role="img" aria-label="Large house with front lawn"></div>
    <div class="row"><span class="name">The Orvelle Mall</span><span class="city">New Dehli</span></div>
    <div class="row2"><span>Retail Malls</span><span><svg width="7" height="10" viewBox="0 0 10 14"><path d="M5 0a5 5 0 0 1 5 5c0 4-5 9-5 9S0 9 0 5a5 5 0 0 1 5-5z" fill="#444"/></svg>Lakeview Road</span></div>
    <div class="cta">View The Listing</div>
  </article>
</main>

<footer>
  <div class="abs footer">
    <div class="abs fcol" style="left:171px">
      <h4>LATEST NEWS</h4>
      <p style="margin-top:22px">Post your Retail Space requirement with us and our.</p>
      <p class="date">1 March, 2014</p>
      <p style="margin-top:10px">Post your Retail Space requirement with us and our.</p>
      <p class="date">1 March, 2014</p>
    </div>
    <div class="abs fcol" style="left:390px">
      <h4>EDITORS CHOICE</h4>
      <p style="margin-top:22px">Post your Retail Space requirement with us and our experts shall get back with suitable options and even help you in your transaction.</p>
      <div class="btn-more">MORE</div>
    </div>
    <div class="abs fcol" style="left:610px">
      <h4>USEFUL LINKS</h4>
      <ul><li>About Us</li><li>Privacy Policy</li><li>Terms of Use</li><li>Contact Us</li><li>Site Map</li></ul>
    </div>
    <div class="abs fcol" style="left:829px">
      <h4>OUR NEWSLETTER</h4>
      <p style="margin-top:22px">Post your Retail Space requirement with us and our experts shall get back with suitable options!</p>
      <div class="input-email">EMAIL</div>
      <div class="btn-send">SEND</div>
    </div>
  </div>
  <div class="abs bottom">
    <div class="abs bottom-brand"><i></i>kelvoranet</div>
    <div class="abs copyright">Copyright © 2014, <span>Vantrel Retail Hub.com</span>. All rights reserved.</div>
    <div class="abs social"><i></i><i></i><i></i><i></i></div>
  </div>
</footer>

</body>
</html>
```